Package for a Mouthfreshener called VORA!!

We are looking for an awesome packaging design for a bran new product called “Vora Mouthfreshener”

This product is going to be made in USA so is really importar that ‘Made in USA” is part of the packaging.

We also need to include the ingredients that are going to be the following:
Saffron
cardamom
menthol
catechu
permited spices and falvors
tree nuts.

We are looking to haver this in a green or purple color and to clarify that the “best before” is for 2 years after the production date

Target Market(s)

Indian stores in usa

Colors
0094D4
00A9DD
6FCCEA
C7EBF8
E9F6FB
00AB8E
00BBA5
67D7C9
C6EFE9
E9F9F6
6B429C
8869AF
B7A5CE
E3DAEB
F3F0F8

Requirements
Must have
• Ingredients
Nice to have
• A good font and is important to mention is made in USA on images I upload an idea for the font

```html
<!DOCTYPE html>
<html lang="en">
<head>
<meta charset="utf-8">
<title>Vora Mouthfreshener – Sachet</title>
<link href="https://fonts.googleapis.com/css2?family=Lato:ital,wght@0,900;1,700;1,900&display=swap" rel="stylesheet">
<style>
  :root {
    --page-bg: #f0f0f0;
    --purple-deep: #5e0668;
    --purple-dark: #7a0a88;
    --purple-mid: #9a10aa;
    --magenta: #c43ccc;
    --pink-light: #ea6cf0;
    --green: #00bf12;
    --green-edge: #b2f7b6;
    --ring: #111111;
    --placeholder: #8a7f99;
    --white: #ffffff;
    --pink-white: #fde6fd;
  }
  html, body {
    margin: 0;
    padding: 0;
    width: 1200px;
    height: 1072px;
    overflow: hidden;
    background: var(--page-bg);
  }
  .canvas {
    position: relative;
    width: 1200px;
    height: 1072px;
  }
  .sachet {
    position: absolute;
    left: 391px;
    top: 219px;
    width: 425px;
    height: 619px;
    display: block;
  }
  .sachet .body { fill: var(--purple-dark); }
  .sachet .band-top { fill: var(--purple-deep); }
  .sachet .band-upper { fill: var(--magenta); }
  .sachet .band-green-edge { fill: var(--green-edge); }
  .sachet .band-green { fill: var(--green); }
  .sachet .band-pink { fill: var(--pink-light); }
  .sachet .band-ingredients { fill: var(--purple-mid); }
  .sachet .band-bottom { fill: var(--purple-deep); }
  .sachet .crimp { fill: var(--purple-dark); }
  .sachet .badge-ring { fill: var(--ring); }
  .sachet .badge-artwork { fill: var(--placeholder); }
  .sachet .badge-label {
    fill: var(--white);
    font-family: "Lato", sans-serif;
    font-weight: 900;
    font-size: 34px;
    letter-spacing: 2px;
  }
  .sachet .brand-name {
    fill: var(--white);
    font-family: "Lato", sans-serif;
    font-weight: 900;
    font-size: 250px;
  }
  .sachet .product-type {
    fill: var(--pink-white);
    font-family: "Lato", sans-serif;
    font-style: italic;
    font-weight: 900;
    font-size: 70px;
  }
  .sachet .ingredients {
    fill: var(--white);
    font-family: "Lato", sans-serif;
    font-style: italic;
    font-weight: 700;
    font-size: 34px;
  }
</style>
</head>
<body>
<main class="canvas">
  <svg class="sachet" viewBox="0 0 692 1007" xmlns="http://www.w3.org/2000/svg" aria-label="Vora Mouthfreshener sachet">
    <defs>
      <pattern id="crimp-top" width="18" height="16" patternUnits="userSpaceOnUse">
        <polygon class="crimp" points="0,16 9,0 18,16"/>
      </pattern>
      <pattern id="crimp-bottom" width="18" height="16" patternUnits="userSpaceOnUse">
        <polygon class="crimp" points="0,0 9,16 18,0"/>
      </pattern>
      <path id="badge-arc" d="M110,335 A224,224 0 0,1 558,335"/>
    </defs>

    <rect x="0" y="0" width="692" height="16" fill="url(#crimp-top)"/>
    <rect x="0" y="991" width="692" height="16" fill="url(#crimp-bottom)"/>

    <rect class="body" x="0" y="16" width="692" height="975"/>
    <polygon class="band-top" points="0,16 692,16 692,45 0,168"/>
    <polygon class="band-upper" points="0,168 692,45 692,250 0,430"/>

    <g class="badge">
      <circle class="badge-ring" cx="334" cy="335" r="245"/>
      <circle class="badge-artwork" cx="334" cy="335" r="203" role="img" aria-label="Flag artwork for the made in USA badge"/>
      <text class="badge-label" dominant-baseline="middle">
        <textPath href="#badge-arc" startOffset="392">MADE IN USA</textPath>
      </text>
    </g>

    <polygon class="band-green-edge" points="0,415 692,235 692,592 0,772"/>
    <polygon class="band-green" points="0,440 692,260 692,567 0,747"/>
    <polygon class="band-pink" points="0,772 692,592 692,712 0,882"/>
    <polygon class="band-ingredients" points="0,882 692,712 692,880 0,955"/>
    <polygon class="band-bottom" points="0,955 692,880 692,991 0,991"/>

    <text class="brand-name" x="350" y="600" text-anchor="middle" transform="rotate(-15 350 520)">Vora</text>
    <text class="product-type" x="362" y="752" text-anchor="middle" transform="rotate(-15 362 730)">Mouthfreshener</text>

    <text class="ingredients" text-anchor="middle">
      <tspan x="338" y="879">Contains: Saffron, cardamom, menthol,</tspan>
      <tspan x="338" y="911">catechu, permited spices and falvors,</tspan>
      <tspan x="338" y="943">tree nuts.</tspan>
    </text>
  </svg>
</main>
</body>
</html>
```